LM Hair and Beauty flyer

Hello I have hairdressing salon called LM Hair and Beauty.I need flyer with double side pls.On front side I need this picture to be there and under the pisture our full address,tel number and email address( 48 Penwick rd E7 3QD 02084417396 media@lmhairandbeauty.co.uk). And under that shoud be written:Special offers
with 3 different discount squares at the bottom of the flyer.First visite 20% off,Second 15% off, thrd 10% off.At he other side of flyer should be following info:Ladies cut & blowdry with 3 different levels of stylist £45-£65,Gents cut £15-£36,Highlights from £45-£120,Express Blowdry £22-£35,Keratin tretmant £150,Manicure from £14,Pedicure from £25,Shellac from £28

Industry/Entity Type

Salon

```html
<!DOCTYPE html>
<html lang="en">
<head>
<meta charset="utf-8">
<title>LM Hair and Beauty flyer</title>
<link href="https://fonts.googleapis.com/css2?family=Roboto+Condensed:wght@300;400;500&family=Italianno&display=swap" rel="stylesheet">
<style>
  :root {
    --backdrop: #d8d2ce;
    --taupe: #7e6c69;
    --taupe-light: #8d7c79;
    --ink: #161212;
    --paper: #ffffff;
    --numeral: #7a6a67;
    --photo-light: #cfc3bf;
    --photo-mid: #8b7774;
    --photo-dark: #3e3030;
  }
  * { box-sizing: border-box; margin: 0; padding: 0; }
  html, body { width: 1200px; height: 892px; overflow: hidden; }
  body {
    background: var(--backdrop);
    position: relative;
    font-family: "Roboto Condensed", "Arial Narrow", sans-serif;
  }
  .side { position: absolute; top: 86px; width: 506px; height: 719px; overflow: hidden; }
  .front { left: 93px; background: var(--paper); }
  .back { left: 600px; background: var(--taupe); }

  /* front */
  .team-photo {
    position: absolute; left: 0; top: 0; width: 505px; height: 470px;
    background: radial-gradient(ellipse at 50% 35%, var(--photo-light) 0%, var(--photo-mid) 55%, var(--photo-dark) 100%);
  }
  .photo-edge { position: absolute; left: 0; top: 0; width: 505px; height: 719px; }
  .brand-row {
    position: absolute; left: 100px; top: 420px; display: flex; align-items: center; gap: 14px;
  }
  .brand-dot { width: 80px; height: 80px; border-radius: 50%; background: var(--ink); }
  .brand-name { font-size: 27px; font-weight: 300; color: var(--ink); letter-spacing: 0.5px; text-transform: uppercase; }

  .offers { position: absolute; left: 0; top: 536px; width: 505px; height: 150px; }
  .offers-frame { position: absolute; left: 67px; top: 18px; width: 372px; height: 22px;
    border: 1.5px solid var(--taupe); border-bottom: none; }
  .offers-title {
    position: absolute; left: 165px; top: 0; width: 174px; height: 29px;
    background: var(--taupe); color: var(--paper);
    font-size: 20px; text-align: center; line-height: 29px; letter-spacing: 0.5px;
  }
  .visit { position: absolute; top: 46px; font-size: 9px; color: var(--taupe); text-transform: uppercase; letter-spacing: 0.3px; display: flex; align-items: center; gap: 3px; }
  .visit::before, .visit::after { content: ""; display: block; width: 12px; height: 1px; background: var(--taupe); }
  .visit-1 { left: 75px; } .visit-2 { left: 209px; } .visit-3 { left: 356px; }
  .star { position: absolute; color: var(--taupe); font-size: 13px; }
  .discount { position: absolute; top: 56px; font-family: "Italianno", cursive; color: var(--numeral); font-size: 96px; line-height: 1; }
  .discount small { font-size: 16px; }
  .discount-1 { left: 68px; } .discount-2 { left: 212px; } .discount-3 { left: 352px; }

  .contact-bar {
    position: absolute; left: 0; top: 689px; width: 505px; height: 28px; background: var(--ink);
    color: var(--paper); font-size: 14.5px; display: flex; align-items: center; gap: 5px; padding-left: 23px; white-space: nowrap;
  }
  .contact-bar svg { width: 9px; height: 9px; }

  /* back */
  .vertical-name {
    position: absolute; left: 48px; top: 719px; transform-origin: 0 0; transform: rotate(-90deg);
    font-size: 96px; font-weight: 300; color: var(--taupe-light); white-space: nowrap; text-transform: uppercase; line-height: 1;
  }
  .back-brand { position: absolute; left: 216px; top: 27px; display: flex; align-items: center; gap: 10px; }
  .back-brand .brand-dot { width: 74px; height: 74px; background: var(--paper); }
  .back-brand .brand-name { color: var(--paper); font-size: 23px; }
  .price-list { position: absolute; left: 217px; top: 0; list-style: none; }
  .price-item { position: absolute; left: 0; width: 260px; }
  .service { color: var(--ink); font-size: 15.5px; font-weight: 500; text-transform: uppercase; line-height: 18px; }
  .price {
    display: block; width: 111px; height: 35px; margin-top: 6px; background: var(--paper);
    color: var(--taupe); font-size: 24px; line-height: 35px; text-align: center;
  }
</style>
</head>
<body>
  <section class="side front">
    <div class="team-photo" role="img" aria-label="Sepia group photo of the salon team posing inside the salon"></div>
    <svg class="photo-edge" viewBox="0 0 505 719" aria-hidden="true">
      <path d="M0,454 Q252.5,298 505,454 L505,719 L0,719 Z" fill="#ffffff"/>
      <path d="M0,454 Q252.5,298 505,454" fill="none" stroke="#7e6c69" stroke-width="6"/>
    </svg>
    <div class="brand-row">
      <span class="brand-dot"></span>
      <span class="brand-name">LM Hair and Beauty</span>
    </div>
    <div class="offers">
      <div class="offers-frame"></div>
      <div class="offers-title">SPECIAL OFFERS</div>
      <span class="visit visit-1">First visit</span>
      <span class="star" style="left:180px;top:42px">★</span>
      <span class="visit visit-2">Second visit</span>
      <span class="star" style="left:321px;top:42px">★</span>
      <span class="visit visit-3">Third visit</span>
      <span class="discount discount-1">20<small>%off</small></span>
      <span class="star" style="left:180px;top:118px">★</span>
      <span class="discount discount-2">15<small>%off</small></span>
      <span class="star" style="left:321px;top:118px">★</span>
      <span class="discount discount-3">10<small>%off</small></span>
    </div>
    <div class="contact-bar">
      <span>48 Penwick rd E7 3QD</span>
      <svg viewBox="0 0 10 10" aria-hidden="true"><rect width="10" height="10" rx="2" fill="#fff"/><path d="M3 2.5 L4.3 4 L3.7 4.7 Q4.6 6 5.7 6.4 L6.3 5.8 L7.6 7 L6.8 7.8 Q3 7 2.3 3.2 Z" fill="#161212"/></svg>
      <span>02084417396</span>
      <svg viewBox="0 0 10 10" aria-hidden="true"><rect width="10" height="10" rx="2" fill="#fff"/><rect x="2" y="3" width="6" height="4" fill="none" stroke="#161212" stroke-width="0.8"/><path d="M2 3 L5 5.3 L8 3" fill="none" stroke="#161212" stroke-width="0.8"/></svg>
      <span>media@lmhairandbeauty.co.uk</span>
    </div>
  </section>

  <section class="side back">
    <div class="vertical-name" aria-hidden="true">Hair and Beauty</div>
    <div class="back-brand">
      <span class="brand-dot"></span>
      <span class="brand-name">LM Hair and Beauty</span>
    </div>
    <ul class="price-list">
      <li class="price-item" style="top:117px"><div class="service">Ladies cut &amp; blow-dry with<br>3 different levels of stylist</div><span class="price">£45-£65</span></li>
      <li class="price-item" style="top:203px"><div class="service">Gents cut</div><span class="price">£15-£36</span></li>
      <li class="price-item" style="top:270px"><div class="service">Highlights from</div><span class="price">£45-£120</span></li>
      <li class="price-item" style="top:341px"><div class="service">Express blow-dry</div><span class="price">£22-£35</span></li>
      <li class="price-item" style="top:410px"><div class="service">Keratin tretmant</div><span class="price">£150</span></li>
      <li class="price-item" style="top:479px"><div class="service">Manicure from</div><span class="price">£14</span></li>
      <li class="price-item" style="top:548px"><div class="service">Pedicure from</div><span class="price">£25</span></li>
      <li class="price-item" style="top:617px"><div class="service">Shellac from</div><span class="price">£28</span></li>
    </ul>
  </section>
</body>
</html>
```